New business card design needed for Diesel Fitting (Mechanical) Company

We need a new business card for our company called "Gumtree Engine Works" that showcases our logo and business details.
Target Market(s)
Owners of all makes and models of vehicles, trucks, plant and machinery.
Industry/Entity Type
Mechanical
Contact Information for Business Card
The business card details need to include the following: Owners/Directors: Doug & Marisol Brent-Coyle ABN: 41 917 302 846 Address: 317 Wattlebrook Street MULGARRA FLATS QLD 4806 Postal Address: PO Box 5791 MULGARRA FLATS QLD 4806 Website: www.gewservice.com.au Phone: 4712 9083 Mobile: 0438 175 906 Emails: sales@gewservice.com.au; admin@gewservice.com.au; accounts@gewservice.com.au; parts@gewservice.com.au; office@gewservice.com.au, reception@gewservice.com.au
Look and feel

```html
<!DOCTYPE html>
<html lang="en">
<head>
<meta charset="utf-8">
<title>Gumtree Engine Works – Business Card</title>
<link rel="stylesheet" href="https://fonts.googleapis.com/css2?family=Montserrat:wght@400;500;600;700&display=swap">
<style>
  :root {
    --red-bright: #ec2028;
    --red-deep: #b4101b;
    --red-shadow: #8e0d15;
    --ink: #000000;
    --steel-dark: #15191d;
    --steel-mid: #3a434b;
    --accent: #c94405;
    --text: #464646;
    --paper: #ffffff;
  }
  * { margin: 0; padding: 0; box-sizing: border-box; }
  html, body { width: 1200px; height: 686px; overflow: hidden; background: var(--paper); }
  .card {
    position: relative;
    width: 1200px;
    height: 686px;
    overflow: hidden;
    background: var(--paper);
    font-family: "Montserrat", Arial, sans-serif;
    color: var(--text);
  }
  .card__art { position: absolute; inset: 0; width: 1200px; height: 686px; }
  .card__photo { position: absolute; left: 0; top: 0; width: 270px; height: 686px; }

  .brand {
    position: absolute;
    left: 58px;
    top: 300px;
    width: 330px;
    display: flex;
    align-items: center;
    gap: 14px;
    color: var(--paper);
    font-weight: 600;
    font-size: 30px;
    line-height: 1.15;
  }
  .brand__dot {
    flex: none;
    width: 38px;
    height: 38px;
    border-radius: 50%;
    background: var(--paper);
  }

  .owners {
    position: absolute;
    left: 662px;
    top: 124px;
    color: var(--accent);
  }
  .owners__names { font-weight: 700; font-size: 24.8px; letter-spacing: 0.2px; line-height: 1; }
  .owners__role { font-weight: 500; font-size: 28px; line-height: 1; margin-top: 16px; }

  .contact { position: absolute; left: 662px; color: var(--text); font-weight: 500; }
  .contact__icon { position: absolute; left: 0; fill: var(--text); }
  .contact__text { position: absolute; left: 59px; white-space: nowrap; }

  .contact--phone { top: 278px; }
  .contact--phone .contact__icon { top: 11px; width: 36px; height: 42px; }
  .contact--phone .divider { position: absolute; left: 44px; top: 0; width: 4px; height: 65px; background: var(--text); }
  .contact--phone .contact__text { left: 59px; top: -10px; font-size: 26px; line-height: 41px; }

  .contact--email { top: 370px; }
  .contact--email .contact__icon { top: 2px; width: 46px; height: 33px; }
  .contact--email .contact__text { top: 0; font-size: 24px; line-height: 30px; }

  .contact--web { top: 436px; }
  .contact--web .contact__icon { top: 0; width: 44px; height: 44px; }
  .contact--web .contact__text { top: 6px; font-size: 24px; line-height: 30px; }

  .contact--address { top: 504px; }
  .contact--address .contact__icon { left: 5px; top: 0; width: 36px; height: 52px; }
  .contact--address .contact__text { top: 1px; font-size: 19.4px; line-height: 24.5px; }

  .abn {
    position: absolute;
    left: 678px;
    top: 605px;
    font-size: 26.4px;
    font-weight: 500;
    color: var(--text);
  }
</style>
</head>
<body>
<div class="card">
  <svg class="card__art" viewBox="0 0 2016 1152" preserveAspectRatio="none" aria-hidden="true">
    <defs>
      <linearGradient id="steel" x1="0" y1="0" x2="1" y2="0.3">
        <stop offset="0" stop-color="var(--steel-mid)"/>
        <stop offset="0.55" stop-color="var(--steel-dark)"/>
        <stop offset="1" stop-color="#000"/>
      </linearGradient>
      <linearGradient id="corner" x1="0" y1="0" x2="1" y2="0">
        <stop offset="0" stop-color="var(--red-bright)"/>
        <stop offset="1" stop-color="var(--red-deep)"/>
      </linearGradient>
    </defs>
    <polygon points="0,0 455,0 785,580 455,1152 0,1152" fill="url(#steel)"/>
    <polygon points="455,0 625,0 958,580 785,580" fill="var(--red-bright)"/>
    <polygon points="785,580 958,580 625,1152 455,1152" fill="var(--red-deep)"/>
    <polygon points="625,0 672,0 1005,580 672,1152 625,1152 958,580" fill="var(--ink)"/>
    <polygon points="672,0 968,0 862,182 820,255" fill="var(--red-bright)"/>
    <polygon points="672,0 862,182 820,255" fill="var(--red-shadow)"/>
    <polygon points="672,1152 965,1152 820,905" fill="var(--red-bright)"/>
    <polygon points="672,1152 862,978 820,905" fill="var(--red-shadow)"/>
    <path d="M2016,20 L1905,132 Q1860,180 1905,228 L2016,350 Z" fill="url(#corner)"/>
  </svg>
  <div class="card__photo" role="img" aria-label="Dark close-up photograph of engine machinery parts"></div>

  <div class="brand">
    <span class="brand__dot"></span>
    <span class="brand__name">Gumtree Engine Works</span>
  </div>

  <div class="owners">
    <div class="owners__names">DOUG &amp; MARISOL BRENT-COYLE</div>
    <div class="owners__role">Owners/Directors</div>
  </div>

  <div class="contact contact--phone">
    <svg class="contact__icon" viewBox="0 0 24 28" aria-hidden="true">
      <path d="M4 1 L9 1 L11 8 L8 11 Q11 18 16 20 L19 17 L24 19 L24 25 Q24 28 20 28 Q3 25 1 5 Q1 1 4 1 Z"/>
    </svg>
    <span class="divider"></span>
    <div class="contact__text">Phone: 4712 9083<br>Mobile: 0438 175 906</div>
  </div>

  <div class="contact contact--email">
    <svg class="contact__icon" viewBox="0 0 46 33" aria-hidden="true">
      <path d="M0 0 H46 V33 H0 Z M4 4 L23 19 L42 4 Z M3 29 L16 17 L3 7 Z M43 29 L43 7 L30 17 Z M6 29 H40 L27 20 L23 23 L19 20 Z" fill-rule="evenodd"/>
    </svg>
    <div class="contact__text">sales@gewservice.com.au</div>
  </div>

  <div class="contact contact--web">
    <svg class="contact__icon" viewBox="0 0 44 44" aria-hidden="true">
      <circle cx="22" cy="22" r="20" fill="none" stroke="var(--text)" stroke-width="3"/>
      <ellipse cx="22" cy="22" rx="8" ry="20" fill="none" stroke="var(--text)" stroke-width="3"/>
      <rect x="2" y="14" width="40" height="4"/>
      <rect x="2" y="26" width="40" height="4"/>
      <rect x="20" y="2" width="4" height="40"/>
    </svg>
    <div class="contact__text">www.gewservice.com.au</div>
  </div>

  <div class="contact contact--address">
    <svg class="contact__icon" viewBox="0 0 36 52" aria-hidden="true">
      <path d="M18 0 A18 18 0 0 1 36 18 Q36 28 18 52 Q0 28 0 18 A18 18 0 0 1 18 0 Z M18 10 A8 8 0 1 0 18 26 A8 8 0 1 0 18 10 Z" fill-rule="evenodd"/>
    </svg>
    <div class="contact__text">317 Wattlebrook Street, PO Box 5791<br>MULGARRA FLATS QLD 4806</div>
  </div>

  <div class="abn">ABN: 41 917 302 846</div>
</div>
</body>
</html>
```